Trade Show Booth Sign Design for Retracting Banner

I need a trade show booth sign designed. It will be for a retractable banner that is double sided with 34 by 81 inch.

I want to incorporate my logo (see attached, have it in other file formats as well) and graphics from my website (https://www.dolbrookteachingadvisory.com/) with parts or all of the following text.

· Educational Content Creation
o Supplemental Textbook Content Development
o E-learning Content Development
· Curriculum Development
o KVTR/Bright Ladder
o Three Dimensional Learning
· Assessment
o Formative Assessments
o Elementary School, Middle School, High School, College, and Business
· Professional Development
o Training
o Facilitation

Target Market(s)

Education

Industry/Entity Type

Education

Font styles to use
Sans Serif

Colors

Designer to choose colors to be used in the design.

Requirements
Must have
• Eye catching and easy to read design
Nice to have
• Would like to see incorporation of my logo and some of the elements of my website images
Should not have
• N/A

```html
<!DOCTYPE html>
<html lang="en">
<head>
<meta charset="utf-8">
<title>Dolbrook Teaching Advisory – Retractable Banner</title>
<link href="https://fonts.googleapis.com/css2?family=Arimo:wght@400;700&display=swap" rel="stylesheet">
<style>
  :root{
    --stage:#404040;
    --panel-light:#f3f4f5;
    --panel-edge:#c9cbcd;
    --art-top:#d6d7d9;
    --art-warm:#efe3c9;
    --art-bottom:#e8e9ea;
    --navy:#0f2260;
    --orange:#f7a20c;
    --sky:#0cb1ea;
    --slate:#858585;
    --teal:#22c5d9;
    --white:#ffffff;
  }
  *{box-sizing:border-box;margin:0;padding:0}
  html,body{width:1200px;height:1200px;overflow:hidden;background:var(--stage);font-family:"Arimo",Arial,sans-serif}
  .banner{
    position:absolute;left:365px;top:30px;width:470px;height:1140px;overflow:hidden;
    background:radial-gradient(ellipse 70% 55% at 45% 40%,var(--panel-light) 0%,#e2e3e5 55%,var(--panel-edge) 100%);
  }
  .hero-art{
    position:absolute;left:0;top:0;width:470px;height:360px;
    background:linear-gradient(180deg,var(--art-top) 0%,var(--art-warm) 55%,var(--art-bottom) 100%);
  }
  .brand{position:absolute;left:0;width:100%;text-align:center;color:var(--navy);font-weight:700}
  .brand-name{top:398px;font-size:54px;letter-spacing:1px;line-height:1}
  .brand-sub{top:456px;font-size:22px;line-height:1}
  .headline{
    position:absolute;left:0;top:510px;width:100%;text-align:center;
    color:var(--navy);font-size:35px;line-height:1.14;font-weight:400;
  }
  .bubble{
    position:absolute;color:var(--white);font-size:25px;line-height:1.06;
    padding:10px 14px 0 18px;border-radius:12px;
  }
  .bubble::after{content:"";position:absolute;top:100%;width:16px;height:22px;background:inherit}
  .bubble.tail-left::after{left:0;clip-path:polygon(0 0,100% 0,0 100%)}
  .bubble.tail-right::after{right:0;clip-path:polygon(0 0,100% 0,100% 100%)}
  .bubble.elearning{left:237px;top:621px;width:191px;height:105px;background:var(--orange)}
  .bubble.content{left:40px;top:686px;width:184px;height:102px;background:var(--sky)}
  .bubble.pd{left:237px;top:763px;width:191px;height:105px;background:var(--navy);padding-top:18px}
  .bubble.standards{left:40px;top:824px;width:184px;height:102px;background:var(--slate)}
  .bubble.assessment{left:237px;top:905px;width:191px;height:106px;background:var(--teal);padding-top:36px}
  .site-url{
    position:absolute;left:0;top:1076px;width:100%;text-align:center;
    color:var(--navy);font-size:17px;font-weight:700;
  }
  .base-band{position:absolute;left:40px;top:1114px;width:388px;height:26px;background:var(--navy)}
</style>
</head>
<body>
  <main class="banner">
    <div class="hero-art" role="img" aria-label="Illustration of three hanging light bulbs, the centre one glowing orange"></div>
    <div class="brand brand-name">DOLBROOK</div>
    <div class="brand brand-sub">Teaching Advisory</div>
    <h1 class="headline">Research-Based<br>Educational Products</h1>
    <div class="bubble elearning tail-left">E-learning<br>Content<br>Development</div>
    <div class="bubble content tail-right">Educational<br>Content<br>Creation</div>
    <div class="bubble pd tail-left">Professional<br>Development</div>
    <div class="bubble standards tail-right">KVTR/<br>Bright Ladder</div>
    <div class="bubble assessment tail-left">Assessment</div>
    <div class="site-url">www.dolbrookteachingadvisory.com</div>
    <div class="base-band"></div>
  </main>
</body>
</html>
```